Mexican construction company needs a business card design

We need a business card design for a company based in Monterrey, Mexico called:

Desarrollos Tolvani S.A. de C.V.

The company is in the construction business and I would like the businees card to be simple and concise. Please use white background and blue or black text color that say:

"Proyectos de Construcción"-- (Brief description of business)
" Rodrigo Ulloa Benítez"--- (My name)
"rulloab@correovelo.mx"-- (My email)
"C: (81) 82 19 57 46"-- (My cell)
"O: (81) 86 72 13 95"-- (Office phone)

Please use only the colors of my company that are attached

Please make the back of the business card blue (same blue from logo) and use the logo.

Thanks!

```html
<!DOCTYPE html>
<html lang="es">
<head>
<meta charset="utf-8">
<title>Desarrollos Tolvani – Tarjeta de presentación</title>
<link href="https://fonts.googleapis.com/css2?family=Montserrat:wght@600&family=Open+Sans:wght@400;600&display=swap" rel="stylesheet">
<style>
  :root{
    --stage:#000000;
    --paper:#ffffff;
    --navy:#07063f;
    --ink:#1c1c1c;
    --grey:#7a7a7a;
    --rule:#8a8aa6;
  }
  *{margin:0;padding:0;box-sizing:border-box}
  html,body{width:1200px;height:900px;overflow:hidden;background:var(--stage)}
  .canvas{position:relative;width:1200px;height:900px}

  .card{position:absolute;top:275px;width:477px;height:293px}
  .card-front{left:116px;background:var(--paper);border-radius:0 44px 0 44px}
  .card-back{left:622px;background:var(--navy);border-radius:44px 0 44px 0}

  .brand{position:absolute;display:flex;align-items:center;gap:14px;
    font-family:"Montserrat",sans-serif;font-weight:600;text-transform:uppercase;line-height:1}
  .brand-mark{flex:none}
  .brand-name span{display:block}
  .brand-name .line-top{letter-spacing:1.5px}
  .brand-name .line-main{letter-spacing:1px;margin-top:6px}

  .card-front .brand{left:32px;top:40px;color:var(--ink)}
  .card-front .brand-mark{width:70px;height:70px;background:var(--grey)}
  .card-front .line-top{font-size:19px}
  .card-front .line-main{font-size:28px}

  .card-back .brand{left:78px;top:104px;color:var(--paper)}
  .card-back .brand-mark{width:84px;height:84px;background:#8a8a8a}
  .card-back .line-top{font-size:20px}
  .card-back .line-main{font-size:30px}

  .holder{position:absolute;left:0;right:0;top:177px;display:flex;align-items:center}
  .holder .rule{height:1px;background:var(--rule)}
  .holder .rule-long{flex:1}
  .holder .rule-short{width:18px}
  .holder-name{font-family:"Open Sans",sans-serif;font-weight:600;font-size:15px;color:var(--navy);padding:0 5px;white-space:nowrap}

  .contacts{position:absolute;right:22px;top:207px;list-style:none;
    font-family:"Open Sans",sans-serif;font-size:12.5px;color:var(--ink)}
  .contacts li{display:flex;justify-content:flex-end;align-items:center;gap:5px;height:20px}
  .contacts svg{width:14px;height:14px;flex:none}
</style>
</head>
<body>
<div class="canvas">

  <section class="card card-front">
    <div class="brand">
      <div class="brand-mark"></div>
      <div class="brand-name"><span class="line-top">Desarrollos</span><span class="line-main">Tolvani</span></div>
    </div>

    <div class="holder">
      <div class="rule rule-long"></div>
      <p class="holder-name">Rodrigo Ulloa Benítez</p>
      <div class="rule rule-short"></div>
    </div>

    <ul class="contacts">
      <li>(81) 82 19 57 46
        <svg viewBox="0 0 14 14" aria-hidden="true"><rect width="14" height="14" rx="2" fill="#07063f"/><path d="M3.5 8.5h7v2h-7z M4 8.5l1.5-3h3l1.5 3 M4.5 5.5c0-1.5 5-1.5 5 0" fill="none" stroke="#fff" stroke-width="1"/></svg>
      </li>
      <li>(81) 86 72 13 95
        <svg viewBox="0 0 14 14" aria-hidden="true"><rect width="14" height="14" rx="2" fill="#07063f"/><rect x="4.5" y="2.5" width="5" height="9" rx="1" fill="none" stroke="#fff" stroke-width="1"/></svg>
      </li>
      <li>rulloab@correovelo.mx
        <svg viewBox="0 0 14 14" aria-hidden="true"><rect width="14" height="14" rx="2" fill="#07063f"/><rect x="3" y="4.5" width="8" height="5.5" fill="#fff"/><path d="M3 4.5l4 3 4-3" fill="none" stroke="#07063f" stroke-width="0.8"/></svg>
      </li>
    </ul>
  </section>

  <section class="card card-back">
    <div class="brand">
      <div class="brand-mark"></div>
      <div class="brand-name"><span class="line-top">Desarrollos</span><span class="line-main">Tolvani</span></div>
    </div>
  </section>

</div>
</body>
</html>
```